依頼詳細
レスポンシブウェブデザインを意識したデザインでお願いします。
参考URL
https://morisato-koubou.jp/

デザインに関しては、添付してあるデザインレイアウトシートを基にお願いします。

まずはパソコンサイトのデザインをお願いします。
当選後、スマホデザインをお願いします。

既存のテンプレートを使う場合は
テンプレート名を下記のような記載を提案の中にいれてください。
例:WordpressテーマはKandoria、デザインスキンは無料のHLM2019 RX4(http://kandoria.com/ex_plugin/hlmnagoya2019_rx4/)をベースにデザインいたしました。
など

素材となる写真は現在、撮影中ですので、一旦他のサイトや参考URLの写真をサンプルとして入れてください。(サンプルなどの表記をお願いします)
また、購入が必要な写真などを利用した場合は、Pelmora Stock(https://stock.pelmora.com/jp/)からファイル番号と価格を教えてください。
ページ数
1ページ
希望イメージ
シンプル 複雑
単色 カラフル
暗い 明るい
日常 高級
遊び心 厳粛
未来的 伝統的
女性的 男性的
希望する色
茶系、緑系
納品ファイル
• イラストレーター形式 (.ai)
• フォトショップ形式 (.psd)
• PNG形式 (.png)
補足説明
上記のいずれか1つ。アウトラインありとなしの2つ。

クライアントのイメージ通りでした。

たくさんのご提案ありがとうございました。
次回もぜひ、よろしくお願い致します。

```html
<!DOCTYPE html>
<html lang="ja">
<head>
<meta charset="utf-8">
<title>株式会社モリサト</title>
<link href="https://fonts.googleapis.com/css2?family=Noto+Sans+JP:wght@400;500;700&display=swap" rel="stylesheet">
<style>
:root{
  --green:#1f9a47;
  --green-dark:#17803a;
  --text:#333333;
  --muted:#777777;
  --line:#dddddd;
  --gray:#d6d6d6;
  --white:#ffffff;
}
*{margin:0;padding:0;box-sizing:border-box}
html,body{width:1200px;height:3704px;overflow:hidden;background:var(--white)}
body{font-family:"Noto Sans JP",sans-serif;color:var(--text);position:relative}
.abs{position:absolute}
.brand{left:0;width:1200px;display:flex;justify-content:center;align-items:center;gap:10px;font-weight:700;font-size:18px;color:var(--text)}
.brand-mark{width:18px;height:18px;background:var(--green)}
.nav{left:0;width:1200px;display:flex;justify-content:center}
.nav a{display:block;width:110px;text-align:center;font-size:13px;color:var(--text);text-decoration:none;line-height:36px}
.nav a.active{background:var(--green);color:var(--white)}
.hero{top:80px;left:0;width:1200px;height:392px;background:radial-gradient(ellipse at 50% 15%,#e9f6c8 0%,#9fd15f 30%,#4d8f2c 65%,#2d5e1b 100%);display:flex;align-items:center;justify-content:center}
.hero p{color:var(--white);font-size:26px;font-weight:700;letter-spacing:2px;text-shadow:0 1px 4px rgba(0,0,0,.4)}
.sec-title{left:0;width:1200px;text-align:center}
.sec-title h2{font-size:24px;font-weight:700}
.sec-title span{display:block;font-size:11px;color:var(--muted);letter-spacing:1px;margin-top:8px}
.sec-title i{display:block;width:240px;height:3px;background:var(--green);margin:8px auto 0}
.lead{left:0;width:1200px;text-align:center;font-size:20px;font-weight:700}
.features{top:700px;left:150px;width:900px;display:flex;justify-content:space-between}
.feature{width:150px;text-align:center;font-size:13px;line-height:1.6}
.feature .ph{width:140px;height:180px;margin:0 auto 30px;background:linear-gradient(#f3e6cf,#d9bf92);border-radius:4px}
.biz{top:1232px;left:204px;display:flex;gap:40px}
.biz-item{width:168px}
.biz-box{height:168px;background:var(--green);color:var(--white);font-size:24px;font-weight:700;display:flex;align-items:center;justify-content:center;text-align:center;line-height:1.3}
.small{font-size:11px;line-height:1.7;margin-top:16px;color:var(--text)}
.works{top:1712px;left:204px;display:flex;gap:40px}
.work{width:168px;text-align:center;font-size:12px}
.work .ph{height:128px;margin-bottom:24px;background:linear-gradient(135deg,#c9b48c,#8b7656)}
.news{top:2124px;left:200px;width:800px}
.news li{list-style:none;display:flex;gap:24px;font-size:12px;padding:14px 0;border-bottom:1px solid var(--line);height:60px;align-items:center}
.news .cat{color:var(--text);font-weight:500}
.news .t{color:#5566aa}
.blog{top:2512px;left:200px;display:flex;gap:40px}
.post{width:170px}
.post .ph{height:148px;background:var(--gray)}
.post h3{font-size:12px;font-weight:700;text-align:center;margin-top:20px}
.faq{top:2980px;left:200px;width:800px}
.qa{margin-bottom:44px}
.qa .q{color:var(--green);font-size:16px;font-weight:700;padding-bottom:8px;border-bottom:1px solid var(--line)}
.qa .a{font-size:12px;margin-top:12px}
.contact{top:3312px;left:0;width:1200px;height:288px;background:var(--green);color:var(--white);text-align:center}
.contact h2{font-size:22px;font-weight:700;padding-top:48px}
.contact i{display:block;width:240px;height:2px;background:var(--white);margin:10px auto 0}
.contact .co{font-size:17px;font-weight:700;margin-top:34px}
.contact .tel{font-size:24px;font-weight:700;margin-top:14px}
.contact .mail{font-size:20px;font-weight:700;margin-top:6px}
</style>
</head>
<body>
<header>
  <div class="abs brand" style="top:10px"><span class="brand-mark"></span>株式会社モリサト</div>
  <nav class="abs nav" style="top:46px">
    <a class="active">Home</a><a>弊社の強み</a><a>事業案内</a><a>加工事例・商品紹介</a><a>会社案内</a><a>よくある質問</a><a>お問い合わせ</a>
  </nav>
</header>

<section class="abs hero" role="img" aria-label="新緑の大樹を見上げた写真"><p>確かな技術と豊富な実績で、ご要望にお応えします</p></section>

<div class="abs sec-title" style="top:520px"><h2>弊社の強み</h2><span>FEATURE</span><i></i></div>
<p class="abs lead" style="top:630px">豊富な種類の材料をつくりだす幅広い技術力</p>
<div class="abs features">
  <div class="feature"><div class="ph" role="img" aria-label="化粧部材の写真"></div>化粧部材<br>加工・組立</div>
  <div class="feature"><div class="ph" role="img" aria-label="ショーケース部材の写真"></div>産業機器<br>(ショーケース)<br>部材加工・組立</div>
  <div class="feature"><div class="ph" role="img" aria-label="床板パネルの写真"></div>床板<br>パネル加工</div>
  <div class="feature"><div class="ph" role="img" aria-label="梱包製品の写真"></div>梱包製品・<br>梱包資材</div>
  <div class="feature"><div class="ph" role="img" aria-label="加工組立品の写真"></div>その他<br>加工組立</div>
</div>

<div class="abs sec-title" style="top:1110px"><h2>事業案内</h2><span>BUSINESS</span><i></i></div>
<div class="abs biz">
  <div class="biz-item"><div class="biz-box">材料</div><p class="small">テキストが入ります。テキストが入ります。テキストが入ります。テキストが入ります。</p></div>
  <div class="biz-item"><div class="biz-box">加工・組立</div><p class="small">テキストが入ります。テキストが入ります。テキストが入ります。テキストが入ります。</p></div>
  <div class="biz-item"><div class="biz-box">設備</div><p class="small">テキストが入ります。テキストが入ります。テキストが入ります。テキストが入ります。</p></div>
  <div class="biz-item"><div class="biz-box">オーダー<br>メイド</div><p class="small">テキストが入ります。テキストが入ります。テキストが入ります。テキストが入ります。</p></div>
</div>

<div class="abs sec-title" style="top:1594px"><h2>加工事例・商品紹介</h2><span>BUSINESS</span><i></i></div>
<div class="abs works">
  <div class="work"><div class="ph" role="img" aria-label="住宅用ユニット装置部品の写真"></div>住宅用ユニット装置部品</div>
  <div class="work"><div class="ph" role="img" aria-label="木型加工の写真"></div>木型加工</div>
  <div class="work"><div class="ph" role="img" aria-label="建材資材の写真"></div>建材資材</div>
  <div class="work"><div class="ph" role="img" aria-label="パレット製造の写真"></div>パレット製造</div>
</div>

<div class="abs sec-title" style="top:2000px"><h2>お知らせ</h2><span>NEWS</span><i></i></div>
<ul class="abs news">
  <li><span>2019.0.1</span><span class="cat">お知らせ</span><span class="t">テキストが入ります。テキストが入ります。テキストが入ります。</span></li>
  <li><span>2019.0.1</span><span class="cat">お知らせ</span><span class="t">テキストが入ります。テキストが入ります。テキストが入ります。</span></li>
  <li><span>2019.0.1</span><span class="cat">お知らせ</span><span class="t">テキストが入ります。テキストが入ります。テキストが入ります。</span></li>
</ul>

<div class="abs sec-title" style="top:2400px"><h2>ブログ</h2><span>BLOG</span><i></i></div>
<div class="abs blog">
  <div class="post"><div class="ph" role="img" aria-label="ブログ記事のサムネイル"></div><h3>タイトルが入ります</h3><p class="small">テキストが入ります。テキストが入ります。テキストが入ります。</p></div>
  <div class="post"><div class="ph" role="img" aria-label="ブログ記事のサムネイル"></div><h3>タイトルが入ります</h3><p class="small">テキストが入ります。テキストが入ります。テキストが入ります。</p></div>
  <div class="post"><div class="ph" role="img" aria-label="ブログ記事のサムネイル"></div><h3>タイトルが入ります</h3><p class="small">テキストが入ります。テキストが入ります。テキストが入ります。</p></div>
  <div class="post"><div class="ph" role="img" aria-label="ブログ記事のサムネイル"></div><h3>タイトルが入ります</h3><p class="small">テキストが入ります。テキストが入ります。テキストが入ります。</p></div>
</div>

<div class="abs sec-title" style="top:2868px"><h2>よくある質問</h2><span>Q&amp;A</span><i></i></div>
<div class="abs faq">
  <div class="qa"><p class="q">Q. テキストが入ります。テキストが入ります。</p><p class="a">A. テキストが入ります。テキストが入ります。テキストが入ります。</p></div>
  <div class="qa"><p class="q">Q. テキストが入ります。テキストが入ります。</p><p class="a">A. テキストが入ります。テキストが入ります。テキストが入ります。</p></div>
  <div class="qa"><p class="q">Q. テキストが入ります。テキストが入ります。</p><p class="a">A. テキストが入ります。テキストが入ります。テキストが入ります。</p></div>
</div>

<section class="abs contact">
  <h2>お問い合わせはこちら</h2><i></i>
  <p class="co">株式会社モリサト</p>
  <p class="tel">TEL：0000-00-0000</p>
  <p class="mail">MAIL：xxxxxxxx@xxx.xxx</p>
</section>

<footer>
  <nav class="abs nav" style="top:3610px">
    <a>Home</a><a>弊社の強み</a><a>事業案内</a><a>加工事例・商品紹介</a><a>会社案内</a><a>よくある質問</a><a>お問い合わせ</a>
  </nav>
  <div class="abs brand" style="top:3660px"><span class="brand-mark"></span>株式会社モリサト</div>
</footer>
</body>
</html>
```